Wedding design for Leif & Marit (Monogram, Banner, designelements, etc.)

We are looking for a design that goes through the entire wedding from the invitations to decor at the actual wedding party. Specific things we want is a monogram of our initials "L" from "Leif"(Groom) and "M" from "Marit"(Bride). We also want a banner that can be used for, for example webpage / chatterly, and several design elements that can be used for invitations, songs, etc. . We also want our wedding date to come trough, as this is a little special. "18.08.18" is the date and the number "8" is identical to the eternity symbol, something we want to focus on in the design.

Have added some pictures of us, but it's up to the designer and choose if they will be used. And if used, it's great if the design is not locked to some images, but that the images can be replaced afterwards.

Reason: We have now changed the payment guaranteed and specified our wishes

Reason: Many of you have made great monograms (Corbano, Quandr4vix, Olubra, TWatelier and copper vale) But in the brief we have asked for a banner and some designelements we can use in different types of prints. Such as invitations, songs, menus etc.

Industry/Entity Type

Wedding

Font styles to use
Serif
Script

Colors

Designer to choose colors to be used in the design.

Requirements
Must have
• Monogram, Banner for chatterly/webpage, Design elements for use on invitations, songs, signs, and other printed material.
Nice to have
• -Unique/special presentation of our wedding date and names. And nice implementation of the eternity symbol.
• -That the various design components can be used separately as well as together
Should not have
• Not too much details.

```html
<!DOCTYPE html>
<html lang="en">
<head>
<meta charset="utf-8">
<title>Marit &amp; Leif — Wedding Stationery</title>
<link rel="stylesheet" href="https://fonts.googleapis.com/css2?family=Great+Vibes&family=Lobster&family=Oswald:wght@300;400;500&display=swap">
<style>
  :root {
    --backdrop-light: #a9a9ab;
    --backdrop-dark: #7c7c7e;
    --paper: #ffffff;
    --ink: #1c2230;
    --night: #12161f;
    --night-soft: #1d2431;
    --gold: #c8974f;
    --gold-light: #ebc98f;
    --gold-pale: #f4e6cc;
    --shadow: rgba(40, 30, 20, 0.35);
  }
  * { box-sizing: border-box; margin: 0; padding: 0; }
  html, body { width: 1200px; height: 1200px; overflow: hidden; }
  body {
    position: relative;
    background: linear-gradient(180deg, var(--backdrop-dark), var(--backdrop-light));
    font-family: "Oswald", "Arial Narrow", sans-serif;
  }
  .card {
    position: absolute;
    overflow: hidden;
    box-shadow: -10px 10px 0 -2px #d8c29a, -14px 16px 18px var(--shadow);
  }
  .card--light { background: var(--paper); color: var(--ink); }
  .card--dark { background: radial-gradient(ellipse at 50% 40%, var(--night-soft), var(--night)); color: #fff; }

  .invitation { left: 90px; top: 90px; width: 494px; height: 692px; }
  .save-date { left: 638px; top: 90px; width: 494px; height: 692px; }
  .rsvp { left: 90px; top: 836px; width: 350px; height: 262px; }
  .thanks { left: 495px; top: 836px; width: 350px; height: 262px; }
  .tag { left: 900px; top: 880px; width: 233px; height: 174px; }

  .abs { position: absolute; }
  .center-x { left: 0; right: 0; text-align: center; }

  .mandala-area { position: absolute; border-radius: 50%; }
  .ornament {
    position: absolute;
    height: 18px;
    border-radius: 50%;
    background: radial-gradient(ellipse at center, var(--gold-light), var(--gold) 45%, transparent 72%);
  }
  .rule { position: absolute; height: 2px; background: var(--gold); }

  /* Invitation */
  .invitation .mandala-area {
    left: -3px; top: -250px; width: 500px; height: 550px;
    background: radial-gradient(circle at 50% 45%, #f0d6a4 0%, #e4bd7c 35%, #f3e2c2 60%, rgba(255,255,255,0) 72%);
  }
  .script-heavy {
    font-family: "Lobster", cursive;
    color: var(--ink);
    text-shadow: 0 0 0 #fff, 2px 2px 0 #fff, -2px -2px 0 #fff, 2px -2px 0 #fff, -2px 2px 0 #fff;
  }
  .invitation .word-the { top: 118px; font-size: 54px; left: 0; right: 0; text-align: center; padding-left: 20px; }
  .invitation .word-wedding { top: 186px; font-size: 96px; left: 0; right: 0; text-align: center; }
  .invitation .word-of { top: 292px; font-size: 54px; left: 0; right: 0; text-align: center; padding-right: 24px; }
  .name-banner {
    position: absolute; left: 58px; top: 372px; width: 378px; height: 74px;
    background: var(--ink);
    clip-path: polygon(0 0, 100% 0, 96% 50%, 100% 100%, 0 100%, 4% 50%);
    display: flex; align-items: center; justify-content: center;
  }
  .name-banner::before {
    content: ""; position: absolute; inset: 6px 10px;
    border-top: 1.5px solid var(--gold); border-bottom: 1.5px solid var(--gold);
  }
  .name-banner span {
    font-family: "Oswald", sans-serif; font-weight: 400;
    font-size: 50px; letter-spacing: 3px; color: var(--gold-pale);
  }
  .details {
    position: absolute; left: 0; right: 0; top: 506px; height: 98px;
    display: flex; flex-direction: column; justify-content: center; align-items: center;
    font-weight: 300; font-size: 24px; letter-spacing: 1.5px; line-height: 32px; color: var(--ink);
  }

  /* Save the date */
  .save-date .mandala-area {
    left: 56px; top: 60px; width: 380px; height: 380px;
    background: radial-gradient(circle, #6b5232 0%, #b8894a 40%, #d7a964 58%, #8a6a3f 74%, rgba(18,22,31,0) 78%);
  }
  .medallion {
    position: absolute; left: 134px; top: 138px; width: 224px; height: 224px;
    border-radius: 50%; background: var(--night);
    border: 3px double var(--gold);
    box-shadow: 0 0 0 6px var(--night), 0 0 0 8px var(--gold);
  }
  .caps-light { font-family: "Oswald", sans-serif; font-weight: 300; letter-spacing: 0.5px; }
  .save-date .our { top: 164px; font-size: 22px; }
  .save-date .wedding-day { top: 192px; font-size: 22px; }
  .dotted { position: absolute; border-top: 2px dotted var(--gold); }
  .script { font-family: "Great Vibes", cursive; }
  .save-date .name-one { top: 226px; left: 162px; font-size: 44px; }
  .save-date .name-two { top: 268px; left: 176px; font-size: 44px; }
  .save-date .amp { top: 240px; left: 286px; font-size: 52px; color: var(--gold); }
  .save-date .std { top: 526px; font-size: 40px; }
  .save-date .date { top: 566px; font-size: 24px; letter-spacing: 1.5px; }

  /* RSVP */
  .rsvp .mandala-tl {
    left: -120px; top: -110px; width: 300px; height: 300px;
    background: radial-gradient(circle, rgba(232,205,160,0.5), rgba(244,230,204,0.35) 55%, rgba(255,255,255,0) 70%);
  }
  .rsvp .mandala-br {
    left: 280px; top: 110px; width: 200px; height: 200px;
    background: radial-gradient(circle, rgba(232,205,160,0.5), rgba(244,230,204,0.3) 55%, rgba(255,255,255,0) 70%);
  }
  .rsvp .title { top: 38px; font-size: 42px; padding-left: 8px; text-align: center; width: 260px; left: 46px; }
  .rsvp .ink-ornament { background: radial-gradient(ellipse at center, var(--ink), #3b4356 45%, transparent 72%); }
  .write-line { position: absolute; left: 50px; width: 252px; height: 1px; background: var(--ink); }
  .choice {
    position: absolute; left: 94px; display: flex; align-items: center; gap: 8px;
    font-size: 12.5px; font-weight: 400; letter-spacing: 0.3px;
  }
  .choice i { display: block; width: 11px; height: 11px; border: 1px solid var(--ink); }
  .rsvp .deadline { top: 236px; left: 0; width: 352px; text-align: center; font-size: 12.5px; font-weight: 400; }

  /* Thank you */
  .thanks .mandala-tl {
    left: -90px; top: -120px; width: 240px; height: 240px;
    background: radial-gradient(circle, rgba(120,125,135,0.35), rgba(80,85,95,0.25) 55%, rgba(18,22,31,0) 70%);
  }
  .thanks .mandala-br {
    left: 200px; top: 90px; width: 260px; height: 260px;
    background: radial-gradient(circle, rgba(120,125,135,0.35), rgba(80,85,95,0.25) 55%, rgba(18,22,31,0) 70%);
  }
  .thanks .message {
    top: 96px; left: 0; right: 0; text-align: center;
    font-size: 64px; color: var(--gold); transform: rotate(-8deg);
  }

  /* Name tag */
  .tag .names { top: 70px; font-size: 40px; }
  .tag .names .amp { color: var(--gold); font-size: 30px; }
</style>
</head>
<body>

  <section class="card card--light invitation" aria-label="Wedding invitation">
    <div class="mandala-area" role="img" aria-label="Gold mandala ornament"></div>
    <div class="abs script-heavy word-the">the</div>
    <div class="abs script-heavy word-wedding">Wedding</div>
    <div class="abs script-heavy word-of">of</div>
    <div class="name-banner"><span>MARIT &amp; LEIF</span></div>
    <div class="ornament" style="left:130px; top:478px; width:234px;" role="img" aria-label="Gold scroll ornament"></div>
    <div class="rule" style="left:58px; top:505px; width:378px;"></div>
    <div class="details">
      <p>18 AUGUST 2018 / 5.00 - 11.00 PM</p>
      <p>SREET RESTAURANT ADDRESS</p>
      <p>NORHAVEN. 418902</p>
    </div>
    <div class="rule" style="left:58px; top:603px; width:378px;"></div>
    <div class="ornament" style="left:130px; top:614px; width:234px;" role="img" aria-label="Gold scroll ornament"></div>
  </section>

  <section class="card card--dark save-date" aria-label="Save the date card">
    <div class="mandala-area" role="img" aria-label="Gold mandala ornament"></div>
    <div class="medallion"></div>
    <div class="abs center-x caps-light our">OUR</div>
    <div class="abs center-x caps-light wedding-day">WEDDING DAY</div>
    <div class="dotted" style="left:172px; top:222px; width:150px;"></div>
    <div class="abs script name-one">Marit</div>
    <div class="abs script name-two">Leif</div>
    <div class="abs script amp">&amp;</div>
    <div class="ornament" style="left:132px; top:484px; width:230px;" role="img" aria-label="Gold filigree ornament"></div>
    <div class="rule" style="left:92px; top:514px; width:310px; height:1.5px;"></div>
    <div class="abs center-x script std">Save the Date</div>
    <div class="abs center-x caps-light date">18 AUGUST 2018</div>
    <div class="rule" style="left:92px; top:602px; width:310px; height:1.5px;"></div>
    <div class="ornament" style="left:132px; top:612px; width:230px;" role="img" aria-label="Gold filigree ornament"></div>
  </section>

  <section class="card card--light rsvp" aria-label="RSVP card">
    <div class="mandala-area mandala-tl" role="img" aria-label="Faint gold mandala ornament"></div>
    <div class="mandala-area mandala-br" role="img" aria-label="Faint gold mandala ornament"></div>
    <div class="ornament ink-ornament" style="left:126px; top:16px; width:100px;" role="img" aria-label="Dark filigree ornament"></div>
    <div class="dotted" style="left:100px; top:32px; width:162px; border-color:var(--ink); border-top-width:1px;"></div>
    <div class="abs script-heavy title">RSVP</div>
    <div class="rule" style="left:92px; top:94px; width:170px; height:1px; background:var(--ink);"></div>
    <div class="ornament ink-ornament" style="left:126px; top:98px; width:100px;" role="img" aria-label="Dark filigree ornament"></div>
    <div class="write-line" style="top:146px;"></div>
    <div class="write-line" style="top:176px;"></div>
    <div class="choice" style="top:186px;"><i></i>DECLINES WITH REGRET</div>
    <div class="choice" style="top:208px;"><i></i>ACCEPTS WITH PLEASURE</div>
    <div class="abs deadline">KINDLY RESPOND BY 20 SEPTEMBER 2020</div>
  </section>

  <section class="card card--dark thanks" aria-label="Thank you card">
    <div class="mandala-area mandala-tl" role="img" aria-label="Faint grey mandala ornament"></div>
    <div class="mandala-area mandala-br" role="img" aria-label="Faint grey mandala ornament"></div>
    <div class="abs script message">Thank You</div>
  </section>

  <section class="card card--dark tag" aria-label="Name card">
    <div class="ornament" style="left:68px; top:38px; width:97px;" role="img" aria-label="Gold filigree ornament"></div>
    <div class="rule" style="left:20px; top:56px; width:193px; height:1px;"></div>
    <div class="abs center-x script names">Marit <span class="amp">&amp;</span> Leif</div>
    <div class="rule" style="left:20px; top:114px; width:193px; height:1px;"></div>
    <div class="ornament" style="left:68px; top:118px; width:97px;" role="img" aria-label="Gold filigree ornament"></div>
  </section>

</body>
</html>
```